Business Card Design

Business Card for professional consulting firm working with large financial institutions.

Target Market(s)

Executive buyers

Industry/Entity Type

Banking

Contact Information for Business Card

Mild creativity wanted. Not boring, but do elaborate artwork.

Font styles to use
Serif
Sans Serif

Colors

Designer to choose colors to be used in the design.

Requirements
Must have
• Standard business card features - company name, individual name, telephone, website, email, locations.
Nice to have
• Two colors
Should not have
• too many colors, fancy printing, cartoons.

```html
<!DOCTYPE html>
<html lang="en">
<head>
<meta charset="utf-8">
<title>Corelane Advisory – Business Card</title>
<link href="https://fonts.googleapis.com/css2?family=Montserrat:wght@400;500;600&display=swap" rel="stylesheet">
<style>
  :root {
    --page-bg: #e9e9e9;
    --card-white: #ffffff;
    --grey-light: #bdbdbd;
    --grey-dark: #8a8a8a;
    --ink: #1a1a1a;
    --logo-grey: #3a3a3a;
    --text-light: #ffffff;
    --text-soft: #f1f1f1;
  }
  * { margin: 0; padding: 0; box-sizing: border-box; }
  html, body {
    width: 1200px; height: 675px; overflow: hidden;
    background: var(--page-bg);
    font-family: "Montserrat", sans-serif;
  }
  .card {
    position: absolute;
    top: 195px;
    width: 500px; height: 286px;
    background: var(--card-white);
    box-shadow: 0 6px 18px rgba(0,0,0,0.18);
    overflow: hidden;
  }
  .card--front { left: 60px; }
  .card--back { left: 640px; }

  .brand {
    display: flex; align-items: center; gap: 10px;
    color: var(--logo-grey);
    font-family: "Montserrat", sans-serif;
    font-weight: 500;
    letter-spacing: 0.02em;
    white-space: nowrap;
  }
  .brand__dot {
    border-radius: 50%;
    background: var(--grey-light);
    flex: none;
  }
  .card--front .brand {
    position: absolute; left: 50%; top: 50%;
    transform: translate(-50%, -50%);
    font-size: 30px;
  }
  .card--front .brand__dot { width: 16px; height: 16px; }

  .back-art { position: absolute; inset: 0; width: 100%; height: 100%; }
  .card--back .brand {
    position: absolute; right: 22px; top: 58px;
    font-size: 15px; gap: 7px;
  }
  .card--back .brand__dot { width: 10px; height: 10px; }

  .contact {
    position: absolute; left: 26px; top: 34px;
    color: var(--text-light);
  }
  .contact__name { font-size: 19px; font-weight: 600; letter-spacing: 0.03em; }
  .contact__role { font-size: 10px; font-weight: 400; color: var(--text-soft); margin-top: 2px; }
  .contact__list { list-style: none; margin-top: 14px; }
  .contact__item {
    display: flex; align-items: flex-start; gap: 9px;
    font-size: 9px; line-height: 1.35; color: var(--text-soft);
    margin-bottom: 7px;
  }
  .contact__icon { flex: none; width: 13px; height: 13px; }
  .contact__web { font-size: 9px; color: var(--text-soft); margin-top: 6px; }
</style>
</head>
<body>

<section class="card card--front" aria-label="Card front">
  <div class="brand"><span class="brand__dot"></span>Corelane Advisory</div>
</section>

<section class="card card--back" aria-label="Card back">
  <svg class="back-art" viewBox="0 0 500 286" preserveAspectRatio="none" aria-hidden="true">
    <defs>
      <linearGradient id="greyPanel" x1="0" y1="0" x2="1" y2="1">
        <stop offset="0" stop-color="#b8b8b8"/>
        <stop offset="1" stop-color="#8c8c8c"/>
      </linearGradient>
      <linearGradient id="whitePanel" x1="0" y1="0" x2="1" y2="1">
        <stop offset="0" stop-color="#ffffff"/>
        <stop offset="1" stop-color="#ededed"/>
      </linearGradient>
    </defs>
    <rect width="500" height="286" fill="url(#greyPanel)"/>
    <path d="M276 60 C250 140 260 220 294 286 L310 286 C278 218 270 140 292 52 Z" fill="#111"/>
    <path d="M302 0 C262 70 266 200 312 286 L500 286 L500 0 Z" fill="url(#whitePanel)"/>
  </svg>

  <div class="contact">
    <p class="contact__name">Arjun Mehta CA JP</p>
    <p class="contact__role">Director</p>
    <ul class="contact__list">
      <li class="contact__item">
        <svg class="contact__icon" viewBox="0 0 14 14" aria-hidden="true"><circle cx="7" cy="7" r="7" fill="#222"/><rect x="3.5" y="4.6" width="7" height="4.8" fill="none" stroke="#fff" stroke-width="0.9"/><path d="M3.5 4.6 L7 7.4 L10.5 4.6" fill="none" stroke="#fff" stroke-width="0.9"/></svg>
        <span>amehta@corelaneadvisory.com.au</span>
      </li>
      <li class="contact__item">
        <svg class="contact__icon" viewBox="0 0 14 14" aria-hidden="true"><circle cx="7" cy="7" r="7" fill="#222"/><path d="M7 11 C4.6 8 4.4 7 4.4 6 A2.6 2.6 0 0 1 9.6 6 C9.6 7 9.4 8 7 11 Z" fill="#fff"/><circle cx="7" cy="6" r="0.9" fill="#222"/></svg>
        <span>Suite 210, 14 Harbour Lane<br>Castle Ridge NSW 2150</span>
      </li>
      <li class="contact__item">
        <svg class="contact__icon" viewBox="0 0 14 14" aria-hidden="true"><circle cx="7" cy="7" r="7" fill="#222"/><path d="M4.6 3.8 L6 3.6 L6.6 5.6 L5.7 6.3 C6.2 7.4 6.8 8 7.8 8.5 L8.5 7.6 L10.4 8.2 L10.2 9.6 C7 10 4 7 4.6 3.8 Z" fill="#fff"/></svg>
        <span>0400 123 456 &nbsp;&nbsp; 02 9000 1234</span>
      </li>
    </ul>
    <p class="contact__web">www.corelaneadvisory.com.au</p>
  </div>

  <div class="brand"><span class="brand__dot"></span>Corelane Advisory</div>
</section>

</body>
</html>
```